当社は、神戸で埋蔵文化財発掘調査を行う会社として営業しております。
この業界では、全国的に有名ではあるのですが、この度、新たな顧客獲得の一つのアイテムとしてDMを検討しております。
一般的にそんな仕事が存在している事の認識が低く、シンプルでインパクトの強いDMのデザインの作成をお願いします。

①DMデザインの作成(B5サイズ)
②表面 当社ロゴ、住所、TEL、FAX、URL
③裏面 シンプルでインパクトのあるもの

埋蔵文化財発掘調査について詳しく無い方も沢山おられると思いますので、
当社HP http://www.tamurakensa.com/ で確認してください。

イラストレーター形式
PDF形式
質疑回答を元に、裏面を尚且つシンプルで埋蔵文化財発掘調査をインパクトあるデザインをお願いします。
尚、ハガキとして郵送の予定です。

シンプルかつインパクトのあるデザインで、受け取り手にも会社の内容が伝わりやすいと思い採用させて頂きました。

たくさんのご提案頂きまして、誠にありがとうございます。
選考中も非常に悩むデザインが多く、選考に時間が掛かってしまいました。
本当にありがとうございました。

```html
<!DOCTYPE html>
<html lang="ja">
<head>
<meta charset="utf-8">
<title>埋蔵文化財発掘調査業務 DM</title>
<link href="https://fonts.googleapis.com/css2?family=Noto+Sans+JP:wght@400;500;700;900&display=swap" rel="stylesheet">
<style>
:root{
  --green:#1d6a4e;
  --green-dark:#145a40;
  --text:#333;
  --paper:#fff;
  --strip:#8a8f8c;
  --clay:#b79a6a;
}
*{margin:0;padding:0;box-sizing:border-box}
html,body{width:844px;height:1200px;overflow:hidden;background:var(--paper)}
body{font-family:"Noto Sans JP",sans-serif;color:var(--text);position:relative}
.artifact{position:absolute;left:250px;top:690px;width:580px;height:430px;
  background:radial-gradient(ellipse at 30% 45%,#d8c19a 0%,#e9dcc4 40%,rgba(255,255,255,0) 70%),
             radial-gradient(circle at 78% 72%,#d4b888 0%,#eadcc2 35%,rgba(255,255,255,0) 55%);}
.title-band{position:absolute;left:0;top:584px;width:844px;height:122px;background:var(--green);padding:14px 0 0 40px}
.title-line{display:flex;color:#fff;font-weight:900;font-size:38px;line-height:48px;letter-spacing:2px}
.title-line span{padding:0 6px;border-left:2px solid rgba(255,255,255,.75)}
.title-line span:first-child{border-left:none;padding-left:0}
.intro{position:absolute;left:40px;top:728px;width:370px;font-size:15px;line-height:26px;font-weight:500;z-index:1}
.intro p+p{margin-top:8px}
.contact{position:absolute;left:40px;top:938px;color:var(--green);font-weight:700;font-size:37px;line-height:46px;z-index:1}
.strip{position:absolute;left:0;top:1124px;width:844px;height:26px;background:linear-gradient(90deg,#6f7471,#a9adaa);color:#fff;font-size:13px;line-height:26px;padding-left:110px;word-spacing:4px}
.strip .url{margin-left:22px;letter-spacing:.5px}
.footer{position:absolute;left:0;top:1152px;width:844px;height:48px;display:flex;align-items:center;padding:0 40px}
.brand{display:flex;align-items:center;gap:12px}
.brand-mark{width:30px;height:30px;border-radius:50%;background:var(--green)}
.brand-name{color:var(--green);font-weight:700;font-size:13px}
.brand-sub{color:var(--green);font-size:10px;font-weight:500;line-height:13px}
.brand-text .brand-name{font-size:24px;line-height:28px;font-weight:700}
.address{margin-left:auto;font-size:11px;line-height:16px;font-weight:500;border-left:1px solid #999;padding-left:12px}
</style>
</head>
<body>
<div class="artifact" role="img" aria-label="縄文土器と古代銅鏡の線画イラスト"></div>

<header class="title-band">
  <div class="title-line"><span>埋</span><span>蔵</span><span>文</span><span>化</span><span>財</span></div>
  <div class="title-line"><span>発</span><span>掘</span><span>調</span><span>査</span><span>業</span><span>務</span></div>
</header>

<section class="intro">
  <p>文化財保護法に基づき建設工事を行うにあたり埋蔵文化財の試掘調査、発掘調査の必要が生じてまいります。</p>
  <p>弊社は、多くの実績を持ち全国においてご対応可能です。些細な事からでもお気軽にご相談ください。</p>
</section>

<div class="contact">
  <div>TEL 078-900-1234</div>
  <div>FAX 078-900-1235</div>
</div>

<div class="strip">詳しくはホームページをご覧ください<span class="url">http://www.tamurakensa.com/</span></div>

<footer class="footer">
  <div class="brand">
    <div class="brand-mark"></div>
    <div class="brand-text">
      <div class="brand-sub">埋蔵文化財発掘調査業務・土木工事・建築工事</div>
      <div class="brand-name">田村建査株式会社</div>
    </div>
  </div>
  <div class="address">〒650-0000<br>兵庫県神戸市西区緑台2丁目5番8号</div>
</footer>
</body>
</html>
```